Velorin Global's Primary Marketing Brochure (Gate Fold Format)

We are looking for a main brochure design to communicate our company's primary mission, the need, where we meet the needs, how we meet the needs, and how the reader can get involved. We would like to see the color palette be similar to the colors of our company logo (attached). We would like to see a brochure design similar to a "gate fold" offering 22"x8.5" fully opened and 5.5"x8.5" when closed. Front panel, inside panels, full spread panel, and back panel. Required Text for each panel and usable picture suggestions are attached along with the company logo. The design should clean, contemporary, and emotionally compelling.

Target Market(s)

40-65 years old male and female, religious-minded

Industry/Entity Type

It Company

Font styles to use
Sans Serif

Requirements
Must have
• include text from attached WORD document.
• Clean, contemporary design
• Color in color palette of agency logo attached

```html
<!DOCTYPE html>
<html lang="en">
<head>
<meta charset="utf-8">
<title>Velorin Global – Gate Fold Brochure</title>
<link href="https://fonts.googleapis.com/css2?family=Open+Sans:wght@400;600;700&display=swap" rel="stylesheet">
<style>
:root{
  --page:#eeeeec;
  --sky-top:#7fc3ee;
  --sky-mid:#a9d8f4;
  --sky-low:#cfe9f8;
  --gold:#b39656;
  --gold-dark:#9c8043;
  --navy:#1d3e78;
  --ink:#1f2530;
  --white:#ffffff;
  --label:#4a4a4a;
  --accent-blue:#3a8fd0;
}
*{box-sizing:border-box;margin:0;padding:0}
html,body{width:1200px;height:1200px;overflow:hidden}
body{background:var(--page);font-family:"Open Sans",Arial,sans-serif;color:var(--ink);position:relative}
.side-label{position:absolute;left:42px;font-size:40px;font-weight:400;color:var(--label);letter-spacing:1px;line-height:1}
.side-label.outside{top:90px}
.side-label.inside{top:626px}
.spread{position:absolute;left:42px;width:1116px;height:431px;overflow:hidden;box-shadow:0 2px 6px rgba(0,0,0,.18)}
.spread.outside{top:142px}
.spread.inside{top:682px}
.panel{position:absolute;top:0;height:100%;overflow:hidden}
.sky{background:linear-gradient(180deg,var(--sky-top) 0%,var(--sky-mid) 55%,var(--sky-low) 100%)}
.gold{background:var(--gold)}
.swoosh{position:absolute;inset:0;pointer-events:none}
.abs{position:absolute}
h2{font-weight:600;color:var(--white);line-height:1.05}
h3{font-weight:600;color:var(--white);font-size:10px;line-height:1.2}
p,li{font-size:6.6px;line-height:1.32}
.bullets{list-style:none}
.bullets li{position:relative;padding-left:7px;margin-bottom:2px}
.bullets li::before{content:"";position:absolute;left:0;top:2px;width:4px;height:4px;border-radius:50%;background:var(--white)}
.photo{position:absolute}
.brand-name{font-weight:600;color:var(--navy);display:flex;align-items:center;gap:6px;white-space:nowrap}
.brand-dot{display:inline-block;border-radius:50%;background:var(--navy)}
.contact{list-style:none}
.contact li{font-size:7px;display:flex;align-items:center;gap:4px;margin-bottom:2.5px}
.contact svg{width:7px;height:7px;flex:none}
.country-col{list-style:none}
.country-col li{font-size:8px;line-height:9.8px;color:var(--ink)}
.area h3{font-size:10px;margin-top:7px}
.area p{margin-top:1px}
.help h3{font-size:10px;margin-top:5px}
.help p{margin-top:1px}
.tagline{font-size:10.5px;font-weight:600;color:var(--white);line-height:1.1}
.worker-copy p{font-size:6.9px;line-height:1.33;margin-bottom:2px}
</style>
</head>
<body>

<div class="side-label outside">OUTSIDE</div>
<div class="side-label inside">INSIDE</div>

<!-- OUTSIDE SPREAD -->
<section class="spread outside">
  <div class="panel sky needs" style="left:0;width:277px">
    <svg class="swoosh" viewBox="0 0 277 431" preserveAspectRatio="none">
      <path d="M0 258 C90 262 190 235 277 205 L277 214 C190 246 90 272 0 268 Z" fill="#fff" opacity=".75"/>
      <path d="M0 248 C90 250 190 226 277 198 L277 203 C190 232 90 256 0 254 Z" fill="#fff" opacity=".4"/>
    </svg>
    <h2 class="abs" style="left:45px;top:22px;font-size:16.5px">Stats of needs from<br>around the world</h2>
    <ul class="bullets abs" style="left:45px;top:62px;width:190px">
      <li>3.11 billion people around the world are unreached and need to hear the Gospel</li>
      <li>About 16,000 children under the age of five die each day from preventable causes</li>
      <li>10.7% of the world's population lives on less than $1.90 per day</li>
      <li>1 out of every 113 people around the world is a refugee</li>
      <li>1-2% of human trafficking victims are ever rescued</li>
      <li>1.2 million children trafficked each year</li>
      <li>The average age of a human trafficking victim is 12. The average age a teen enters the sex trade in the U.S. is 12 to 14-year- old. Many victims are runaway girls who were sexually abused as children.</li>
      <li>More than 85 percent of the pastors around the world have never received theological education or pastoral preparation</li>
    </ul>
    <div class="brand-name abs" style="left:80px;top:286px;font-size:15px"><span class="brand-dot" style="width:13px;height:13px"></span>Velorin Global</div>
    <ul class="contact abs" style="left:50px;top:318px">
      <li><svg viewBox="0 0 10 10"><path d="M5 0a3.5 3.5 0 0 0-3.5 3.5C1.5 6 5 10 5 10s3.5-4 3.5-6.5A3.5 3.5 0 0 0 5 0zm0 5a1.5 1.5 0 1 1 0-3 1.5 1.5 0 0 1 0 3z" fill="#1f2530"/></svg>2140 Harrow Ridge Rd. Larkfield, TN. 37000-0000</li>
      <li><svg viewBox="0 0 10 10"><rect x="1" y="1.5" width="8" height="5.5" fill="#1f2530"/><rect x="0" y="7.5" width="10" height="1.5" fill="#1f2530"/></svg>www.veloringlobal.org</li>
      <li><svg viewBox="0 0 10 10"><path d="M2 1h2l1 2.5-1.3 1a6 6 0 0 0 2.8 2.8l1-1.3L10 7v2a1 1 0 0 1-1 1A9 9 0 0 1 0 1a1 1 0 0 1 1-1z" fill="#1f2530"/></svg>800-555-0142</li>
      <li><svg viewBox="0 0 10 10"><circle cx="5" cy="5" r="4" fill="#1f2530"/></svg>Facebook.com/VelorinGlobal</li>
      <li><svg viewBox="0 0 10 10"><circle cx="5" cy="5" r="4" fill="#1f2530"/></svg>Twitter.com/VELORINGL</li>
    </ul>
    <svg class="abs" style="left:116px;top:378px" width="34" height="34" viewBox="0 0 34 34"><circle cx="17" cy="17" r="15.5" fill="#fff" stroke="#1d3e78" stroke-width="2.5"/></svg>
  </div>

  <div class="panel gold vision" style="left:277px;width:562px">
    <div class="photo" role="img" aria-label="Close-up photo of two young children looking at the camera" style="left:295px;top:138px;width:267px;height:172px;background:linear-gradient(90deg,#5a3a28 0%,#8a5e44 22%,#d9c2a8 42%,#b88464 58%,#e6d2bc 80%,#9a7050 100%)"></div>
    <svg class="swoosh" viewBox="0 0 562 431" preserveAspectRatio="none">
      <path d="M180 112 C300 135 420 120 562 60 L562 0 L300 0 L300 40 C330 80 260 110 180 112 Z" fill="#c8ad6b" opacity=".55"/>
      <path d="M180 112 C300 140 430 128 562 70 L562 80 C430 142 300 152 180 112 Z" fill="#fff" opacity=".85"/>
      <path d="M295 138 C400 128 490 110 562 92 L562 138 Z" fill="#b39656"/>
      <path d="M295 310 C390 292 480 296 562 312 L562 330 C480 314 390 312 295 328 Z" fill="#b39656"/>
      <path d="M295 316 C390 298 480 302 562 318 L562 323 C480 308 390 306 295 322 Z" fill="#fff" opacity=".55"/>
    </svg>
    <h2 class="abs" style="left:21px;top:16px;font-size:15px">Vision of Velorin</h2>
    <p class="abs" style="left:21px;top:38px;width:238px">Our vision is ever more communities all around the world radically transformed by the love of the Gospel... communities with reproducing, multiplying, Christ-centered national leaders who are part of thriving, engaged local churches growing committed disciples of Jesus, boldly proclaiming the Good News, compassionately caring for spiritual and physical needs, and advancing the Kingdom in all aspects of society.</p>
    <h2 class="abs" style="left:21px;top:102px;font-size:15px">Statement of Faith</h2>
    <h3 class="abs" style="left:21px;top:127px;font-size:10px">We believe:</h3>
    <ul class="bullets abs" style="left:21px;top:141px;width:248px">
      <li>in the Scriptures of the Old and New Testament as inspired by God and inerrant in the original writings and that they are the supreme and final authority in faith and life.</li>
      <li>in one God, eternally existing in three persons: Father, Son, and Holy Spirit.</li>
      <li>that Jesus Christ was begotten by the Holy Spirit and born of the virgin Mary and is true God and true man.</li>
      <li>that man was created in the image of God, that he sinned and thereby incurred not only physical death but also that spiritual death which is separation from God, and that all human beings are born with a sinful nature.</li>
      <li>that the Lord Jesus Christ died for our sins, according to the Scriptures, as a representative and substitutionary sacrifice, and that all who believe in Him are justified on the ground of His shed blood.</li>
      <li>in the bodily resurrection of our crucified Lord, His ascension into heaven and His presence there for us as High Priest and Advocate.</li>
      <li>in that "blessed hope" - the personal and victorious return of our Lord and Savior, Jesus Christ.</li>
      <li>that all who receive by repentance and faith the Lord Jesus Christ are born again of the Holy Spirit, and become children of God.</li>
      <li>in the bodily resurrection of the just and unjust, the everlasting blessedness of the saved and the everlasting punishment of the lost.</li>
      <li>that, according to the specific teachings of the entire Bible, which is the written Word of God, God created man and women as unique biological persons made to complete each other, and that human sexuality in God's plan is to be expressed only within the context of monogamous marriage between a genetic male and a genetic female, and that such marriage is the foundation of the family and the basic structure of human society.</li>
    </ul>
    <h2 class="abs" style="left:295px;top:14px;font-size:27px;font-weight:400;line-height:1.1">Equipping the<br>Nations with<br>the Gospel</h2>
    <div class="photo" role="img" aria-label="White dove in flight" style="left:497px;top:24px;width:50px;height:42px;border-radius:4px;background:linear-gradient(135deg,#ffffff 0%,#efe9dc 100%);opacity:.9"></div>
    <div class="brand-name abs" style="left:322px;top:368px;font-size:25px"><span class="brand-dot" style="width:28px;height:28px"></span>Velorin Global</div>
  </div>

  <div class="panel sky countries" style="left:839px;width:277px">
    <svg class="swoosh" viewBox="0 0 277 431" preserveAspectRatio="none">
      <path d="M0 112 C80 80 180 62 277 60 L277 67 C180 70 80 88 0 120 Z" fill="#fff" opacity=".55"/>
      <path d="M0 310 C80 302 180 318 277 340 L277 348 C180 326 80 310 0 318 Z" fill="#fff" opacity=".6"/>
    </svg>
    <h2 class="abs" style="left:31px;top:22px;font-size:16.5px">34 countries<br>where Velorin is present</h2>
    <div class="photo" role="img" aria-label="Dotted world map marking the countries where the ministry is present" style="left:10px;top:72px;width:258px;height:140px;border-radius:6px;background:linear-gradient(180deg,#5f7688 0%,#41586c 50%,#6b8296 100%);opacity:.85"></div>
    <ul class="country-col abs" style="left:78px;top:228px">
      <li>Albania</li><li>Argentina</li><li>Australia</li><li>Bulgaria</li><li>Bangladesh</li><li>Canada</li><li>Costa Rica</li><li>Cuba</li><li>Cyprus</li><li>Egypt</li><li>Greece</li><li>Guatemala</li><li>Ghana</li><li>Haiti</li><li>India</li><li>Indonesia</li><li>Italy</li>
    </ul>
    <ul class="country-col abs" style="left:159px;top:228px">
      <li>Kenya</li><li>Lebanon</li><li>Liberia</li><li>Mexico</li><li>Moldova</li><li>Myanmar</li><li>Pakistan</li><li>Peru</li><li>Philippines</li><li>Romania</li><li>South Africa</li><li>Spain</li><li>Thailand</li><li>Turkey</li><li>Uganda</li><li>United States</li><li>Zimbabwe</li>
    </ul>
  </div>
</section>

<!-- INSIDE SPREAD -->
<section class="spread inside">
  <div class="panel sky worker" style="left:0;width:275px">
    <div class="photo" role="img" aria-label="Portrait photo of a national worker outdoors" style="left:0;top:254px;width:275px;height:177px;background:linear-gradient(90deg,#7c9a80 0%,#a0ae92 28%,#5a3b2a 48%,#3e2a20 66%,#6d4c3a 82%,#9aa7a0 100%)"></div>
    <svg class="swoosh" viewBox="0 0 275 431" preserveAspectRatio="none">
      <path d="M0 240 C90 244 180 258 275 272 L275 254 L0 254 Z" fill="#b8def5"/>
      <path d="M0 244 C90 248 180 262 275 276 L275 282 C180 268 90 254 0 252 Z" fill="#fff" opacity=".7"/>
    </svg>
    <h2 class="abs" style="left:25px;top:12px;font-size:16px">Who is a National Worker?</h2>
    <div class="worker-copy abs" style="left:25px;top:36px;width:222px">
      <p>National workers are native missionaries who reach their own people with the Gospel. They are the hands and feet of Velorin in the countries where we minister.</p>
      <p>National workers are unique. Because they serve in their own countries, they don't need special government residence permits and they are already experts with the local language and culture. They can even serve in countries where cross-cultural missionaries would not be allowed and they serve at a fraction of the cost a foreign missionary would need to raise.</p>
      <p>National workers serve in a variety of ways to empower the local church and advance God's kingdom. Some are church planters and pastors. Some are teachers, school directors, house parents, support staff at Velorin's child and youth development centers educating a new generation of Christ-followers that will strengthen the local churches. Some serve in the medical arena as doctors and nurses. Serving in a variety of ministries that vary based on what is needed in a particular country or area, they are the key and the most effective way to sharing God's love in word and deed, following the example of Jesus Christ.</p>
    </div>
    <div class="tagline abs" style="left:25px;top:218px;width:240px">At the heart of every Velorin ministry<br>is a national worker</div>
    <div class="abs" style="left:2px;top:409px;font-size:14px;font-weight:600;color:var(--white)">Odongo Samuel</div>
    <div class="abs" style="left:0;top:427px;width:118px;height:4px;background:var(--accent-blue)"></div>
  </div>

  <div class="panel gold ministry" style="left:275px;width:564px">
    <div class="photo" role="img" aria-label="Photo of a child carrying water containers on a red dirt road" style="left:241px;top:0;width:323px;height:272px;background:linear-gradient(180deg,#7f9a6e 0%,#93a37a 14%,#c08868 30%,#b6735a 60%,#a4654c 100%)"></div>
    <div class="photo" role="img" aria-label="Photo of a young girl looking up" style="left:0;top:262px;width:230px;height:169px;background:linear-gradient(90deg,#7a6350 0%,#c9b7a6 45%,#e3d6cb 70%,#a48c78 100%)"></div>
    <div class="photo" role="img" aria-label="Photo of a mother in a headscarf holding her baby" style="left:230px;top:262px;width:334px;height:169px;background:linear-gradient(90deg,#3a2c26 0%,#6d5142 30%,#8c6a52 55%,#c8b49c 78%,#a88c72 100%)"></div>
    <svg class="swoosh" viewBox="0 0 564 431" preserveAspectRatio="none">
      <path d="M0 262 C150 276 350 258 564 236 L564 262 L0 262 Z" fill="#b39656"/>
      <path d="M241 250 C350 246 460 240 564 236 L564 272 L241 272 Z" fill="#b39656" opacity="0"/>
      <path d="M0 266 C150 282 350 264 564 242 L564 250 C350 272 150 292 0 276 Z" fill="#fff" opacity=".8"/>
      <path d="M200 0 C300 10 420 12 564 5 L564 0 Z" fill="#fff" opacity=".6"/>
    </svg>
    <h2 class="abs" style="left:24px;top:12px;font-size:16px">5 Areas of Ministry</h2>
    <div class="area abs" style="left:24px;top:32px;width:212px">
      <h3>Child Sponsorship</h3>
      <p>Velorin national workers verbally and visibly share the love of Christ to children which leads to transformed lives physically, intellectually, spiritually, emotionally, and socially.</p>
      <h3>Velorin Disciple Makers</h3>
      <p>Velorin is helping to train pastors with resources typically unavailable to them as well as helping resource church planters as they Advance the Gospel.</p>
      <h3>Velorin Medical Care</h3>
      <p>Showing the love of Christ to those in need can range from hospitals, training facilities, leprosy colonies, mobile units, and many clinics worldwide.</p>
      <h3>Velorin Media Evangelism</h3>
      <p>"Media" can take a wide variety of forms. We work through newspapers, internet, radio and other pieces of literature to share the Gospel in unreached areas.</p>
      <h3>Velorin Disaster Relief</h3>
      <p>Velorin offers help when disasters such as earthquakes, hurricanes, tornadoes, and flooding occur as well as assisting Greece in the refugee crisis.</p>
    </div>
  </div>

  <div class="panel sky help" style="left:839px;width:277px">
    <div class="photo" role="img" aria-label="Photo of a smiling radio host at a studio microphone and mixing desk" style="left:153px;top:0;width:124px;height:246px;background:linear-gradient(180deg,#d9e4ea 0%,#c79a86 22%,#8c4050 48%,#6e2e3c 68%,#b8c6d0 100%)"></div>
    <h2 class="abs" style="left:22px;top:12px;font-size:16px">How Can I Help?</h2>
    <div class="abs" style="left:22px;top:34px;width:126px">
      <p>Velorin Global relies on partners like you to assist in spreading the Gospel both in word and action to those in the most desperate of life circumstances. Velorin partners participate by:</p>
      <h3>Giving</h3>
      <p>Financially supporting Velorin through monthly, quarterly, annual, or one-time gifts. This can be done through our sponsorship programs or general support of the overall mission of Velorin worldwide.</p>
      <h3>Going</h3>
      <p>Serve alongside an Velorin national worker on one of Velorin's many short-term mission team opportunities throughout the year; serve as a mission intern locally or on the foreign field; or even pray about serving as one of Velorin's long-term missionaries.</p>
    </div>
    <div class="abs" style="left:22px;top:250px;width:245px">
      <h3>Praying</h3>
      <p>Join us in praying daily for the Lord's work happening through all of Velorin's ministries. Velorin's monthly newsletter, VELORIN NEWS, contains our daily prayer guide for suggestions on how to pray specifically for Velorin's work around the world</p>
      <h3>Publicizing</h3>
      <p>Tell others about the great work you are supporting and connected to at Velorin. Let your church know about the opportunity to partner with an organization that is advancing the Gospel worldwide. Share using social media to let others know all that is happening through your generosity and partnership with Velorin.</p>
      <p style="margin-top:2px">Your partnership in giving, going, praying, and publicizing the mission of Velorin is a key element that allows us to build upon our 75-year history of equipping national workers, empowering the local church, and transforming communities with the Gospel of Jesus Christ.</p>
      <div class="tagline" style="margin-top:6px">Partner with Velorin Today!</div>
    </div>
  </div>
</section>

</body>
</html>
```